Letter design, envelope design, and more

Hello, we the Varlo Gmbh are looking for our shop. Letter C5. Design does not have to be like a business card, so it can have straight lines. Only the color is important. The logo is the text under VaRLo omit.It should not be playful but Profesionel

Font styles to use
Sans Serif

Colors
0555a3
3176b5
85abd2
85cae6
34a7d8
0792cd
cee9f5
cfdfed
000000

Requirements
Must have
• Color like business card, Please, with the text under VaRLo, Correct address Benkelstr. 4 Zip code 9512 Morsach, as well as Couvert Without addressing only design and logo with VaRlo
Nice to have
• more writing articles
Should not have
• Not too colored, Text under VaRLo, bright colors

```html
<!DOCTYPE html>
<html lang="en">
<head>
<meta charset="utf-8">
<title>Varlo Gmbh – Stationery</title>
<link href="https://fonts.googleapis.com/css2?family=Poppins:wght@300;400;600&display=swap" rel="stylesheet">
<style>
  :root {
    --stage: #dcdcdc;
    --paper: #f6f6f6;
    --navy: #0b2259;
    --slate: #8a909e;
    --ink: #3c3f46;
    --rule: #4a5a80;
  }
  * { margin: 0; padding: 0; box-sizing: border-box; }
  html, body { width: 1200px; height: 877px; overflow: hidden; }
  body { background: var(--stage); font-family: 'Poppins', sans-serif; position: relative; }

  .sheet { position: absolute; background: var(--paper); box-shadow: 0 2px 10px rgba(0,0,0,0.18); overflow: hidden; }
  .sheet svg.decor { position: absolute; left: 0; top: 0; width: 100%; height: 100%; }

  .letter { left: 69px; top: 64px; width: 527px; height: 742px; }
  .envelope-back { left: 614px; top: 269px; width: 531px; height: 241px; }
  .envelope-front { left: 614px; top: 562px; width: 532px; height: 241px; }

  .wordmark { position: absolute; display: flex; align-items: center; gap: 8px; }
  .wordmark .mark-square { background: var(--navy); }
  .wordmark .name { font-weight: 600; color: var(--navy); letter-spacing: 1.5px; line-height: 1; }
  .letter .wordmark { left: 317px; top: 48px; }
  .letter .wordmark .mark-square { width: 36px; height: 36px; }
  .letter .wordmark .name { font-size: 29px; }
  .envelope-front .wordmark { left: 27px; top: 46px; }
  .envelope-front .wordmark .mark-square { width: 34px; height: 34px; }
  .envelope-front .wordmark .name { font-size: 27px; }
  .envelope-back .wordmark { left: 50%; top: 20px; transform: translateX(-50%); }
  .envelope-back .wordmark .mark-square { width: 26px; height: 26px; background: #fff; }
  .envelope-back .wordmark .name { color: #fff; font-size: 22px; }

  .salutation { position: absolute; left: 45px; top: 204px; font-size: 14px; font-weight: 300; color: var(--ink); }
  .letter-body { position: absolute; left: 45px; top: 248px; width: 440px; font-size: 7.6px; line-height: 11.4px; font-weight: 300; color: var(--ink); text-align: justify; }
  .letter-body p { margin-bottom: 11.4px; }
  .closing { position: absolute; left: 45px; top: 486px; font-size: 7.6px; font-weight: 300; color: var(--ink); }
  .signature { position: absolute; left: 42px; top: 516px; width: 100px; height: 40px; background: linear-gradient(90deg, rgba(32,80,170,0.18), rgba(32,80,170,0.06)); border-radius: 4px; }

  .contact { position: absolute; left: 38px; top: 671px; display: flex; font-size: 7.4px; line-height: 10px; color: var(--ink); }
  .contact .address { padding-right: 9px; border-right: 1px solid var(--rule); }
  .contact .reach { padding-left: 9px; }
  .contact .reach span { display: flex; align-items: center; gap: 4px; }
  .contact svg { width: 7px; height: 7px; fill: var(--navy); }
  .footer-rule { position: absolute; left: 38px; top: 695px; width: 146px; height: 1px; background: var(--rule); }
  .web { position: absolute; left: 39px; top: 701px; font-size: 7.6px; letter-spacing: 1px; color: var(--navy); }
</style>
</head>
<body>

  <section class="sheet letter">
    <svg class="decor" viewBox="0 0 527 742" preserveAspectRatio="none">
      <path d="M0 0 H400 C230 4 80 25 0 45 Z" fill="var(--slate)"/>
      <path d="M527 693 C440 725 250 735 120 742 H527 Z" fill="var(--navy)"/>
    </svg>
    <div class="wordmark"><span class="mark-square"></span><span class="name">VaRLo</span></div>

    <p class="salutation">Dear Mr. Brenner,</p>
    <div class="letter-body">
      <p>Lorem ipsum dolor sit amet, consectetur adipiscing elit. Donec orci purus, luctus vitae dignissim eu, iaculis sed purus. Vivamus faucibus, ipsum nec aliquet viverra, leo mauris condimentum ligula, sit amet sagittis enim ligula quis arcu. Nam egestas tortor id nisi porttitor mattis. In tortor ante, ultricies in suscipit a, tempus non massa. Vivamus et auctor mi. Fusce vel massa nulla. Phasellus nec eros mauris, et scelerisque orci.</p>
      <p>Donec malesuada orci vitae nulla accumsan porta a id massa. Quisque accumsan iaculis magna sit amet fringilla. Maecenas consequat, magna eget tincidunt semper, odio nibh rutrum mi, id feugiat ante nisi eu risus. Vestibulum nunc orci, rhoncus a placerat in, ultricies in mi. Cras mattis varius eros, vel fringilla nisi suscipit eget. Quisque scelerisque sagittis nulla at porttitor.</p>
      <p>Sed id augue vitae urna euismod commodo aliquet a quam. Pellentesque arcu velit, cursus et malesuada ut, consequat et diam. Nullam erat sem, rhoncus id ullamcorper vitae, rhoncus et arcu. In ultricies ultricies nulla, ut rutrum nisi iaculis at. Donec eu magna a metus ornare faucibus. Fusce aliquet faucibus ultricies. Morbi semper, est id tincidunt gravida, sem arcu adipiscing lacus, ac bibendum nulla leo eu purus. Quisque nec diam sed risus consectetur a ccumsan quis quis nibh. Vestibulum id purus lorem.</p>
      <p>It is a long established fact that a reader will be distracted by the readable content of a page when looking at its layout. The point of using Lorem Ipsum is that it has a more-or-less normal distribution of letters, as opposed to using 'Content here, content here', making it look like readable English. Many desktop publishing packages</p>
    </div>
    <p class="closing">Sincerely,</p>
    <div class="signature" role="img" aria-label="Handwritten signature of Lukas Brenner"></div>

    <div class="contact">
      <div class="address">Benkelstr. 4<br>9512 Morsach</div>
      <div class="reach">
        <span><svg viewBox="0 0 10 10"><path d="M2 0 L4 2.5 L3 3.8 C3.8 5.4 4.8 6.4 6.2 7 L7.5 6 L10 8 L8.5 10 C4 9.5 0.5 6 0 1.5 Z"/></svg>+41 71 555 02 40</span>
        <span><svg viewBox="0 0 10 10"><path d="M0 2 H10 V8 H0 Z M0 2 L5 5.5 L10 2" fill="var(--navy)" stroke="#fff" stroke-width="0.8"/></svg>info@varlo.ch</span>
      </div>
    </div>
    <div class="footer-rule"></div>
    <p class="web">WWW.VARLO.CH</p>
  </section>

  <section class="sheet envelope-back">
    <svg class="decor" viewBox="0 0 531 241" preserveAspectRatio="none">
      <path d="M0 0 H531 L524 45 C521 62 512 73 490 73 H41 C19 73 10 62 7 45 Z" fill="var(--navy)"/>
    </svg>
    <div class="wordmark"><span class="mark-square"></span><span class="name">VaRlo</span></div>
  </section>

  <section class="sheet envelope-front">
    <svg class="decor" viewBox="0 0 532 241" preserveAspectRatio="none">
      <path d="M0 0 H400 C230 4 80 22 0 40 Z" fill="var(--slate)"/>
      <path d="M532 203 C450 225 270 235 110 241 H532 Z" fill="var(--navy)"/>
    </svg>
    <div class="wordmark"><span class="mark-square"></span><span class="name">VaRLo</span></div>
  </section>

</body>
</html>
```